The Quiet Meadow - a modern wellness brand

Looking for a modern, simple, and clean website for a virtual consulting firm focused on holistic wellness and sustainable living. Want a strong combo of text and photos (really shitty starts are available for reference on www.thequietmeadowhub.example and www.ginaposlund.example for reference - general idea is in the right direction, was too difficult to work through with the wordpress template and nothing laid out correctly)
Needs include:
- strong home / landing page
- ability to schedule (use calend.ly) on the site
- online shop / purchasing POS integration
- blog
-multiple 'services' pages
- about page
- contact page
(attached brand board images for brand style / reference)
Updates
Want more opportunity for designs and feedback
Target Market(s)
women and gay men aged 30-50
Coding
Coded - Design and coding required
Number of Pages Required
5+ page
Colors
Designer to choose only greyscale colors for use in the design.
Requirements
Must have
- the ability for me to update and manage through wordpress when things like pricing, or services change
Should not have
- complicated anything

```html
<!DOCTYPE html>
<html lang="en">
<head>
<meta charset="utf-8">
<title>The Quiet Meadow – Holistic Wellness + Sustainable Living</title>
<link rel="stylesheet" href="https://fonts.googleapis.com/css2?family=Tinos:ital,wght@0,400;0,700;1,400&family=Roboto+Slab:wght@300;400&family=Jost:wght@300;400;500&display=swap">
<style>
:root{
  --ink:#0b0b0b;
  --black:#000;
  --white:#fff;
  --paper:#ffffff;
  --mist:#f5f5f5;
  --fog:#e9e9e9;
  --ash:#cfcfcf;
  --stone:#8a8a8a;
  --slate:#555;
  --accent:#1c1c1c;
  --serif:"Tinos", "Times New Roman", serif;
  --slab:"Roboto Slab", Georgia, serif;
  --sans:"Jost", "Helvetica Neue", Arial, sans-serif;
}
*{box-sizing:border-box;margin:0;padding:0}
html,body{width:1200px;height:3030px;overflow:hidden;background:var(--paper)}
body{position:relative;color:var(--ink);font-family:var(--sans)}
.abs{position:absolute}

/* header */
.site-header{position:absolute;left:0;top:0;width:1200px;height:110px}
.brand{position:absolute;left:145px;top:32px;display:flex;align-items:center;gap:14px}
.brand-dot{width:42px;height:42px;border:1.5px solid var(--slate);border-radius:50%;flex:0 0 auto}
.brand-name{font-family:var(--serif);font-size:17px;letter-spacing:3px;text-transform:uppercase;color:var(--ink);white-space:nowrap}
.main-nav{position:absolute;left:470px;top:44px;display:flex;gap:24px;font-family:var(--serif);font-size:13.5px;white-space:nowrap}
.main-nav a{color:var(--ink);text-decoration:none}
.main-nav .current{font-weight:700;border-bottom:1.5px solid var(--ink)}
.btn{display:inline-block;font-family:var(--serif);font-weight:700;font-size:14px;text-decoration:none;padding:11px 22px;outline:1.5px solid currentColor;outline-offset:3px;white-space:nowrap}
.btn-accent{background:var(--accent);color:var(--white);outline-color:var(--accent)}
.btn-dark{background:var(--black);color:var(--white);outline-color:var(--black)}
.btn-light{background:var(--white);color:var(--ink);outline-color:var(--white)}
.header-cta{position:absolute;left:905px;top:35px;font-size:12.5px;padding:10px 16px}

/* hero */
.hero{position:absolute;left:60px;top:110px;width:1080px;height:510px;overflow:hidden}
.hero-photo{position:absolute;inset:0;background:radial-gradient(ellipse at 60% 30%,#4a4a4a 0%,#262626 45%,#0e0e0e 100%)}
.hero-copy{position:absolute;left:0;right:0;top:180px;text-align:center;color:var(--white)}
.hero-title{font-family:var(--serif);font-weight:700;font-size:48px;letter-spacing:1px;text-transform:uppercase}
.hero-sub{font-family:var(--serif);font-style:italic;font-size:28px;margin-top:2px}
.hero-copy .btn{margin-top:26px}
.hero-wave{position:absolute;left:0;bottom:0;width:1080px;height:110px}

/* welcome */
.welcome{position:absolute;left:0;top:660px;width:1200px;height:420px}
.eyebrow{font-family:var(--sans);font-size:12px;letter-spacing:.5px;text-transform:uppercase;color:var(--ink)}
.section-title{font-family:var(--slab);font-weight:300;font-size:32px;color:var(--ink)}
.welcome-copy{position:absolute;left:240px;top:36px;width:330px}
.welcome-copy .section-title{margin-top:8px;font-size:30px}
.welcome-copy p{font-size:12px;line-height:1.75;color:var(--slate);margin-top:18px}
.welcome-copy .btn{margin-top:30px;font-size:12.5px;padding:10px 20px}
.portrait{position:absolute;left:618px;top:0;width:336px;height:336px}
.portrait-fill{position:absolute;inset:0;border-radius:50%;background:radial-gradient(circle at 50% 40%,#9a9a9a,#5c5c5c 70%,#3a3a3a)}
.portrait svg{position:absolute;inset:0}

/* services */
.services{position:absolute;left:60px;top:1110px;width:1080px;height:560px;background:var(--mist)}
.centered{position:absolute;left:0;right:0;text-align:center}
.service-img{position:absolute;width:225px;height:225px}
.img-yoga{background:linear-gradient(180deg,#e4e1e3 0%,#c0b8bc 55%,#6e6c6e 100%)}
.img-friends{background:linear-gradient(160deg,#d6d2cf 0%,#86766c 55%,#3a322f 100%)}
.service-card{position:absolute;width:197px;height:124px;background:var(--black);color:var(--white);padding:22px 22px}
.service-card h3{font-family:var(--serif);font-weight:700;font-size:17px}
.service-card p{font-size:11px;line-height:1.7;margin-top:12px;color:#e6e6e6}
.services-wave{position:absolute;left:0;bottom:-60px;width:1080px;height:80px}

/* blog */
.blog{position:absolute;left:0;top:1775px;width:1200px;height:480px}
.post{position:absolute;top:130px;width:225px}
.post-img{height:152px}
.img-moving{background:linear-gradient(160deg,#d4c8b8,#958a7e 60%,#4d4640)}
.img-stones{background:linear-gradient(180deg,#ece0c8,#c9a67a 55%,#544639)}
.img-pose{background:linear-gradient(180deg,#544640,#969a8e 60%,#c6c2ba)}
.post-body{height:118px;border-right:2px solid var(--black);padding:18px 22px 0}
.post-body h3{font-family:var(--serif);font-weight:700;font-size:14px}
.post-body p{font-size:9.5px;line-height:1.65;color:var(--slate);margin-top:9px}
.post-body a{display:block;font-family:var(--serif);font-weight:700;font-size:10.5px;color:var(--ink);text-decoration:none;margin-top:10px}

/* together */
.together{position:absolute;left:60px;top:2270px;width:1080px;height:310px}
.together .section-title{font-size:27px;font-weight:400}
.together p{font-size:16px;color:var(--stone);margin-top:12px;letter-spacing:.3px}

/* footer */
.site-footer{position:absolute;left:60px;top:2560px;width:1080px;height:470px}
.footer-bg{position:absolute;left:0;top:0;width:1080px;height:470px}
.footer-brand{position:absolute;left:40px;top:170px;width:280px;display:flex;flex-direction:column;align-items:center;gap:20px}
.footer-brand .brand-dot{width:76px;height:76px;border-color:var(--ash)}
.footer-brand .brand-name{color:var(--white);font-size:19px;letter-spacing:3.5px}
.footer-col{position:absolute;color:var(--white)}
.footer-col h4{font-family:var(--serif);font-weight:700;font-size:14px;letter-spacing:.4px;color:var(--white)}
.contact-list{list-style:none;margin-top:18px}
.contact-list li{display:flex;gap:12px;font-size:11px;line-height:1.7;margin-bottom:12px}
.contact-list svg{flex:0 0 12px;margin-top:3px}
.socials{display:flex;gap:7px;margin-top:18px}
.socials span{width:24px;height:24px;border-radius:50%;background:#6d6d6d}
.socials span.on{background:var(--white)}
.form-grid{display:grid;grid-template-columns:141px 141px;gap:10px 8px;margin-top:18px}
.field{border:1px solid #5a5a5a;height:23px;font-size:9px;color:#bdbdbd;padding:5px 12px}
.field.wide{grid-column:1 / 3;height:48px}
.footer-col .btn{margin-top:14px;font-size:10px;padding:7px 16px}
.copyright{position:absolute;left:70px;top:420px;font-size:8.5px;color:#9a9a9a}
.copyright strong{color:var(--white);font-weight:500}
</style>
</head>
<body>

<header class="site-header">
  <div class="brand"><span class="brand-dot"></span><span class="brand-name">The Quiet Meadow</span></div>
  <nav class="main-nav">
    <a class="current" href="#">Home</a>
    <a href="#">About Us</a>
    <a href="#">Services</a>
    <a href="#">Shop</a>
    <a href="#">Blog</a>
    <a href="#">Contact Us</a>
  </nav>
  <a class="btn btn-accent header-cta" href="#">Schedule a Consultation</a>
</header>

<section class="hero">
  <div class="hero-photo" role="img" aria-label="Dark monochrome photo of wild grasses and meadow flowers"></div>
  <div class="hero-copy">
    <h1 class="hero-title">Gina Poslund</h1>
    <p class="hero-sub">Holistic Wellness + Sustainable Living</p>
    <a class="btn btn-light" href="#">Contact Us</a>
  </div>
  <svg class="hero-wave" viewBox="0 0 1080 110" preserveAspectRatio="none">
    <path d="M0 20 C180 90 360 20 540 50 C720 80 880 10 1080 0 L1080 110 L0 110 Z" fill="#fff"/>
    <path d="M0 40 C200 120 380 60 560 60 C740 60 880 40 1080 20" fill="none" stroke="#000" stroke-width="4"/>
  </svg>
</section>

<section class="welcome">
  <div class="welcome-copy">
    <div class="eyebrow">Welcome to</div>
    <h2 class="section-title">The Quiet Meadow</h2>
    <p>Over the last decade and a half, this site has transformed along with me. Beginning as a blog in my early twenties, this site chronicled my musings on life and growth. It was the first space I had to write, process and share how I was experiencing the world; and good, bad, or otherwise, how the world was also experiencing me …</p>
    <p>As the years passed it became a repository for my online resume, businesses, and archived work products when I didn't have another space to house centrally …</p>
    <a class="btn btn-accent" href="#">Discover More</a>
  </div>
  <div class="portrait">
    <div class="portrait-fill" role="img" aria-label="Black and white portrait photo of the wellness consultant"></div>
    <svg viewBox="0 0 336 336"><circle cx="168" cy="168" r="152" fill="none" stroke="#fff" stroke-width="7" stroke-linecap="round" stroke-dasharray="0 16"/></svg>
  </div>
</section>

<section class="services">
  <div class="centered" style="top:50px">
    <div class="eyebrow">What we do</div>
    <h2 class="section-title" style="margin-top:10px">Services We Provide</h2>
  </div>
  <div class="service-img img-yoga" style="left:180px;top:145px" role="img" aria-label="Woman doing a yoga lunge on the beach at sunset"></div>
  <div class="service-card" style="left:331px;top:286px">
    <h3>Holistic Wellness</h3>
    <p>Lorem Ipsum is simply dummy text of the printing and typesetting industry …</p>
  </div>
  <div class="service-img img-friends" style="left:551px;top:145px" role="img" aria-label="Two women reading a book together"></div>
  <div class="service-card" style="left:702px;top:286px">
    <h3>Sustainable Living</h3>
    <p>Lorem Ipsum is simply dummy text of the printing and typesetting industry …</p>
  </div>
  <div class="centered" style="top:465px"><a class="btn btn-dark" href="#" style="font-size:11px;padding:8px 16px">View All Services</a></div>
  <svg class="services-wave" viewBox="0 0 1080 80" preserveAspectRatio="none">
    <path d="M0 0 L1080 0 L1080 20 C900 60 760 70 560 50 C380 30 200 60 0 20 Z" fill="#f5f5f5"/>
    <path d="M380 40 C500 20 700 25 860 40 C700 70 520 70 380 40 Z" fill="#dcdcdc"/>
  </svg>
</section>

<section class="blog">
  <div class="centered" style="top:0">
    <div class="eyebrow">Recent articles</div>
    <h2 class="section-title" style="margin-top:10px">Latest Blog</h2>
  </div>
  <article class="post" style="left:240px">
    <div class="post-img img-moving" role="img" aria-label="Couple relaxing among moving boxes"></div>
    <div class="post-body"><h3>Lorem Ipsum simply</h3><p>It is a long established fact that a reader will be distracted by the readable content of a page when …</p><a href="#">Read More</a></div>
  </article>
  <article class="post" style="left:487px">
    <div class="post-img img-stones" role="img" aria-label="Stacked stones at sunrise"></div>
    <div class="post-body"><h3>Lorem Ipsum simply</h3><p>It is a long established fact that a reader will be distracted by the readable content of a page when …</p><a href="#">Read More</a></div>
  </article>
  <article class="post" style="left:734px">
    <div class="post-img img-pose" role="img" aria-label="Woman in a yoga pose under a wooden pavilion"></div>
    <div class="post-body"><h3>Lorem Ipsum simply</h3><p>It is a long established fact that a reader will be distracted by the readable content of a page when …</p><a href="#">Read More</a></div>
  </article>
  <div class="centered" style="top:430px"><a class="btn btn-accent" href="#" style="font-size:11px;padding:8px 26px">View All</a></div>
</section>

<section class="together">
  <svg class="abs" style="left:0;top:0" width="1080" height="310" viewBox="0 0 1080 310" preserveAspectRatio="none">
    <path d="M0 60 C200 20 360 0 560 0 C760 0 900 30 1080 60 L1080 310 L0 310 Z" fill="#e9e9e9"/>
    <path d="M140 55 C300 10 500 -5 700 20 C500 15 320 30 140 55 Z" fill="#d2d2d2"/>
  </svg>
  <div class="centered" style="top:100px">
    <h2 class="section-title">Let's Work Together.</h2>
    <p>Lorem Ipsum is simply dummy text of the printing</p>
    <div style="margin-top:28px"><a class="btn btn-dark" href="#" style="font-size:11px;padding:8px 22px">Contact Us</a></div>
  </div>
</section>

<footer class="site-footer">
  <svg class="footer-bg" viewBox="0 0 1080 470" preserveAspectRatio="none">
    <path d="M0 0 C220 40 420 40 600 30 C800 18 960 5 1080 0 L1080 470 L0 470 Z" fill="#000"/>
    <path d="M300 36 C480 20 700 10 900 18 C720 40 520 48 300 36 Z" fill="#cfcfcf"/>
  </svg>
  <div class="footer-brand"><span class="brand-dot"></span><span class="brand-name">The Quiet Meadow</span></div>
  <div class="footer-col" style="left:366px;top:150px">
    <h4>Contact Us</h4>
    <ul class="contact-list">
      <li><svg width="12" height="12" viewBox="0 0 12 12"><path d="M2 1 L4.5 1 L5.5 3.5 L4 4.6 C4.7 6 6 7.3 7.4 8 L8.5 6.5 L11 7.5 L11 10 C6 10.5 1.5 6 2 1 Z" fill="none" stroke="#ccc" stroke-width="1"/></svg>+1 (555) 014-2290</li>
      <li><svg width="12" height="12" viewBox="0 0 12 12"><rect x="1" y="2.5" width="10" height="7" fill="none" stroke="#ccc"/><path d="M1 2.5 L6 6.5 L11 2.5" fill="none" stroke="#ccc"/></svg>hello@thequietmeadowhub.example</li>
      <li><svg width="12" height="12" viewBox="0 0 12 12"><path d="M6 11 C3 7.5 2.5 6 2.5 4.5 A3.5 3.5 0 0 1 9.5 4.5 C9.5 6 9 7.5 6 11 Z" fill="none" stroke="#ccc"/><circle cx="6" cy="4.5" r="1.2" fill="#ccc"/></svg><span>48 Fernwood Lane, Millbrook<br>working Area NR 00000</span></li>
    </ul>
    <h4 style="margin-top:20px">Follow Us</h4>
    <div class="socials"><span></span><span class="on"></span><span></span><span></span></div>
  </div>
  <div class="footer-col" style="left:620px;top:150px">
    <h4>Get a Free Counsultion</h4>
    <div class="form-grid">
      <div class="field">Your Name</div><div class="field">Email</div>
      <div class="field">Phone</div><div class="field">Services</div>
      <div class="field wide">Message ...</div>
    </div>
    <a class="btn btn-light" href="#">Send</a>
  </div>
  <p class="copyright">© 2022 <strong>The Quiet Meadow</strong>. All Right Reserved</p>
</footer>

</body>
</html>
```